Business Card Design Project

New business cards that encompass our new logo.
Looking for -
Name, Title, Cell Phone, Email, Address (2 lines), Main Phone, Fax, and website.
Reason: I don't like the graphics used to show phone, fax, cell, email, web, and address.....
I like the double sided cards with logo's on the back. I do not like the logos for phone, fax, cell, address, email, or web.

```html
<!DOCTYPE html>
<html lang="en">
<head>
<meta charset="utf-8">
<title>Northfield Restaurant Supply – Business Card</title>
<link href="https://fonts.googleapis.com/css2?family=Montserrat:wght@600;700;800&family=Michroma&display=swap" rel="stylesheet">
<style>
  :root {
    --bg: #e4e4e4;
    --card: #ffffff;
    --navy: #1f4389;
    --red: #c0303f;
    --band: #b8202f;
    --white: #ffffff;
  }
  * { box-sizing: border-box; margin: 0; padding: 0; }
  html, body { width: 1200px; height: 900px; overflow: hidden; }
  body { background: var(--bg); font-family: "Montserrat", Arial, sans-serif; position: relative; }

  .card {
    position: absolute; left: 150px; top: 190px;
    width: 900px; height: 520px;
    background: var(--card); border-radius: 36px;
    box-shadow: 0 10px 30px rgba(0,0,0,0.12);
    overflow: hidden;
  }
  .brand {
    position: absolute; left: 0; right: 0; top: 70px;
    text-align: center; color: var(--navy);
    font-weight: 800; font-size: 50px; line-height: 1.1;
    letter-spacing: 1px; text-transform: uppercase;
  }
  .tagline-band {
    position: absolute; left: 0; right: 0; top: 248px; height: 34px;
    background: var(--band); color: var(--white);
    font-family: "Michroma", Arial, sans-serif;
    font-size: 17px; letter-spacing: 6px; text-transform: uppercase;
    display: flex; align-items: center; justify-content: center;
  }
  .divider {
    position: absolute; left: 470px; top: 305px; width: 2px; height: 190px;
    background: var(--navy);
  }
  .person {
    position: absolute; right: 445px; top: 362px; text-align: right;
  }
  .person-name { color: var(--red); font-weight: 700; font-size: 34px; line-height: 1.1; }
  .person-title { color: var(--navy); font-weight: 700; font-size: 19px; margin-top: 4px; }

  .contact-list {
    position: absolute; left: 495px; top: 305px; list-style: none;
    color: var(--navy); font-weight: 700; font-size: 21px; line-height: 28px;
  }
  .contact-list li { display: flex; align-items: flex-start; gap: 6px; }
  .contact-icon { width: 24px; height: 24px; flex: none; margin-top: 2px; fill: var(--red); }
</style>
</head>
<body>
  <main class="card">
    <div class="brand">Northfield<br>Restaurant Supply</div>

    <div class="tagline-band">For your all restaurant equipment needs</div>

    <div class="person">
      <div class="person-name">Daniel Reyes</div>
      <div class="person-title">Managing Director</div>
    </div>

    <div class="divider"></div>

    <ul class="contact-list">
      <li>
        <svg class="contact-icon" viewBox="0 0 24 24" aria-hidden="true"><rect x="6" y="2" width="12" height="20" rx="2"/><rect x="8" y="5" width="8" height="8" fill="#fff"/><rect x="8" y="15" width="8" height="4" fill="#fff"/></svg>
        <span>555-014-2287</span>
      </li>
      <li>
        <svg class="contact-icon" viewBox="0 0 24 24" aria-hidden="true"><path d="M6.6 10.8a15 15 0 0 0 6.6 6.6l2.2-2.2c.3-.3.7-.4 1-.2 1.1.4 2.3.6 3.6.6.6 0 1 .4 1 1V20c0 .6-.4 1-1 1A17 17 0 0 1 3 4c0-.6.4-1 1-1h3.5c.6 0 1 .4 1 1 0 1.3.2 2.5.6 3.6.1.3 0 .7-.2 1z"/></svg>
        <span>555-014-3190</span>
      </li>
      <li>
        <svg class="contact-icon" viewBox="0 0 24 24" aria-hidden="true"><rect x="6" y="2" width="11" height="7" fill="none" stroke="#c0303f" stroke-width="2"/><rect x="2" y="9" width="20" height="9" rx="2"/><rect x="6" y="15" width="12" height="7" fill="#fff" stroke="#c0303f" stroke-width="2"/></svg>
        <span>555-014-3125</span>
      </li>
      <li>
        <svg class="contact-icon" viewBox="0 0 24 24" aria-hidden="true"><rect x="2" y="5" width="20" height="14" rx="1"/><path d="M3 6l9 7 9-7" fill="none" stroke="#fff" stroke-width="2"/></svg>
        <span>info@northfieldsupply.com</span>
      </li>
      <li>
        <svg class="contact-icon" viewBox="0 0 24 24" aria-hidden="true"><circle cx="12" cy="12" r="10"/><g fill="none" stroke="#fff" stroke-width="1.5"><ellipse cx="12" cy="12" rx="4" ry="10"/><path d="M2 12h20M4 7h16M4 17h16"/></g></svg>
        <span>www.northfieldsupply.com</span>
      </li>
      <li>
        <svg class="contact-icon" viewBox="0 0 24 24" aria-hidden="true"><path d="M12 2L1 12h3v10h6v-6h4v6h6V12h3z"/></svg>
        <span>4820 Ridgeview Road,<br>Millbrook, CO 80100</span>
      </li>
    </ul>
  </main>
</body>
</html>
```